Website Design for Business Law Firm

We have a logo and now we would like a web site design for our new website. Our small firm provides creative and aggressive transactional (not litigation) legal services to advise healthcare, technology, internet-based and traditional companies and investors in such companies on healthcare, technology, financing, mergers/acquisitions, real estate and other transactions, legal compliance and general corporate and business matters.

We would like to see a website design that is professional and appropriate for executives, professionals, investors and government regulators to visit, that conveys professionalism and competence while being a little edgy and modern - no typical legal motifs such as gavels, books, or scales of justice. We advise businesses and investors and guide them through complicated issues quickly, capably and differently from other law firms. We are part of the business team and get things done.

The logo is attached, and we like gray as a color to complement it. The intention of the logo is to convey that in a storm or challenging time, people come to this firm, and people come to this firm when they need the power and disruption to change things or shake them up.

I have also enclosed a picture of our business card for consideration.

On the other hand, you can check out the current simple site at www.quenlow.example to see we have used a space motif in the past to evoke that we help create stars (the nebula featured there). This is not a necessary part of the new website and it may look better without it.

We appreciate your creativity and look forward to designs.

Industry/Entity Type

Business

Requirements
Must have
• We anticipate the following pages, and you may submit different ideas for the different pages:
• 1. Landing page
• 2. Services pages - healthcare, IT/Technology, general counsel services, financings, mergers/acquisitions, mediation/arbitration, procurement and productization
• 3. About Us including contact information
• Our name and contact information:
• Quenlow Law Firm, P.C.
• 7816 SW 19th Ave.
• Portland, OR 97213
• phone: 555.614.2873
• fax: 555.730.4158
Nice to have
• Please consider designs that enhance the impressions we are looking for
Should not have
• Please no gavels, scales of justice, law books, or similar traditional legal imagery.

```html
<!DOCTYPE html>
<html lang="en">
<head>
<meta charset="utf-8">
<title>Quenlow Law Firm</title>
<link href="https://fonts.googleapis.com/css2?family=Open+Sans:wght@400;600&family=PT+Serif:wght@400&display=swap" rel="stylesheet">
<style>
:root{
  --navy:#1b2a44;
  --navy-deep:#13203a;
  --sky:#d3e6f6;
  --white:#ffffff;
  --teal:#4d6c7c;
  --text:#8a8a8a;
  --heading:#5c5c5c;
  --nav-text:#2b3a4d;
  --button:#a99c9e;
  --card-band:rgba(25,25,25,.85);
}
*{margin:0;padding:0;box-sizing:border-box}
html,body{width:1141px;height:1200px;overflow:hidden}
body{background:var(--sky);font-family:"Open Sans",sans-serif;position:relative}
.header{position:absolute;left:0;top:0;width:1141px;height:165px;background:var(--navy)}
.brand{position:absolute;left:106px;top:31px;width:339px;height:89px;background:var(--white);padding:5px}
.brand-inner{width:100%;height:100%;background:var(--navy-deep);display:flex;align-items:center;justify-content:center;
  font-family:"PT Serif",serif;font-size:44px;letter-spacing:14px;color:var(--white)}
.header-phone{position:absolute;left:878px;top:46px;display:flex;align-items:center;gap:10px;color:var(--white);
  font-family:"PT Serif",serif;font-size:18px;letter-spacing:.5px}
.search{position:absolute;left:847px;top:78px;width:181px;height:21px;background:var(--white);border-radius:2px;overflow:hidden}
.search-btn{position:absolute;right:0;top:0;width:28px;height:21px;background:#9a9a9a;display:flex;align-items:center;justify-content:center}
.nav{position:absolute;left:105px;top:145px;width:932px;height:56px;background:var(--white);border-top:4px solid var(--teal);border-left:5px solid var(--navy);
  display:flex;align-items:center;justify-content:space-around;padding:0 6px;font-size:12.5px;color:var(--nav-text)}
.nav .active{font-weight:600}
.hero{position:absolute;left:105px;top:218px;width:932px;height:336px;
  background:linear-gradient(90deg,#ece8e5 0%,#e6dfd9 30%,#c9b9a8 50%,#6b5a4c 70%,#3a3030 85%,#8a6a48 100%)}
.callout{position:absolute;left:73px;top:288px;width:413px;height:87px;background:var(--navy);color:var(--white);
  font-family:"PT Serif",serif;padding:9px 0 0 41px;white-space:nowrap;overflow:hidden}
.callout-fold{position:absolute;left:73px;top:375px}
.callout-title{font-size:20px;line-height:28px;letter-spacing:-.2px}
.callout-phone{font-size:30px;line-height:40px;letter-spacing:1px}
.cta-shadow{position:absolute;left:119px;top:413px;width:124px;height:40px;background:var(--navy)}
.cta{position:absolute;left:126px;top:418px;width:123px;height:40px;background:var(--button);color:var(--white);border:1px solid #c9c0c0;
  font-family:"PT Serif",serif;font-size:19px;display:flex;align-items:center;justify-content:center}
.content{position:absolute;left:105px;top:576px;width:932px;height:571px;background:var(--white);border-bottom:3px solid var(--navy)}
.welcome{position:absolute;left:11px;top:30px;width:584px}
.section-title{font-size:18px;color:var(--heading);font-weight:400;margin-bottom:9px}
.welcome p{font-size:12.3px;line-height:17.2px;letter-spacing:.25px;color:var(--text);margin-bottom:34px}
.divider{position:absolute;left:629px;top:21px;height:315px;border-left:2px dotted #aaaaaa}
.news{position:absolute;left:645px;top:26px;width:280px}
.news-item{display:flex;gap:8px;height:98px}
.thumb{width:89px;height:60px;flex:none}
.news-item h3{font-size:11.5px;font-weight:600;color:var(--heading);margin:2px 0 8px}
.news-item p{font-size:10.5px;line-height:14px;color:var(--text);max-width:200px}
.issues-title{position:absolute;left:0;top:383px;width:932px;text-align:center;font-family:"PT Serif",serif;font-size:15px;font-weight:400;color:#6f6f6f}
.card{position:absolute;top:403px;width:271px;height:148px}
.card-band{position:absolute;left:0;top:0;width:100%;height:27px;background:var(--card-band);color:var(--white);
  font-family:"PT Serif",serif;font-size:17px;text-align:center;line-height:27px}
.footer{position:absolute;left:0;top:1166px;width:1141px;text-align:center;font-size:11.5px;color:#3d3d3d}
</style>
</head>
<body>
<header class="header">
  <div class="brand"><div class="brand-inner">QUENLOW</div></div>
  <div class="header-phone">
    <svg width="20" height="20" viewBox="0 0 20 20" aria-hidden="true"><rect x="1" y="4" width="5" height="14" fill="#fff"/><rect x="7" y="1" width="11" height="17" fill="none" stroke="#fff" stroke-width="2"/><rect x="10" y="5" width="5" height="3" fill="#fff"/><rect x="10" y="10" width="5" height="5" fill="#fff"/></svg>
    <span>555-730-4158</span>
  </div>
  <div class="search"><div class="search-btn"><svg width="14" height="14" viewBox="0 0 14 14" aria-hidden="true"><circle cx="6" cy="6" r="4.2" fill="none" stroke="#fff" stroke-width="2"/><line x1="9" y1="9" x2="13" y2="13" stroke="#fff" stroke-width="2"/></svg></div></div>
</header>
<nav class="nav">
  <span class="active">HOME</span><span>About Us</span><span>Firm Profile</span><span>Our Cases</span><span>Practice Areas</span><span>Recent Verdicts</span><span>Law Review</span><span>Contact Us</span>
</nav>
<div class="hero" role="img" aria-label="Photo of a smiling team of business lawyers in suits"></div>
<div class="callout">
  <div class="callout-title">Call us today for a Legal Consultation</div>
  <div class="callout-phone">555-730-4158</div>
</div>
<svg class="callout-fold" width="32" height="19" viewBox="0 0 32 19" aria-hidden="true"><polygon points="0,0 32,0 32,19" fill="#2a1a1a"/></svg>
<div class="cta-shadow"></div>
<div class="cta">Click Here</div>
<main class="content">
  <section class="welcome">
    <h2 class="section-title">Welcome to Our Website</h2>
    <p>It is a long established fact that a reader will be distracted by the readable content of a page when looking at its layout. The point of using Lorem Ipsum is that it has a more-or-less normal distribution of letters, as opposed to using 'Content here, content here', making it look like readable English. Many desktop publishing packages and web page editors now use Lorem Ipsum as their default model text, and a search for 'lorem ipsum' will uncover many web sites still in their infancy. Various versions have evolved over the years, sometimes by accident, sometimes on purpose (injected humour and the like).</p>
    <p>It is a long established fact that a reader will be distracted by the readable content of a page when looking at its layout. The point of using Lorem Ipsum is that it has a more-or-less normal distribution of letters, as opposed to using 'Content here, content here', making it look like readable English. Many desktop publishing packages and web page editors now use Lorem Ipsum as their default model text, and a search for 'lorem ipsum'</p>
  </section>
  <div class="divider"></div>
  <section class="news">
    <h2 class="section-title" style="margin-bottom:24px">Our News</h2>
    <div class="news-item"><div class="thumb" role="img" aria-label="Photo of a town street with shops" style="background:linear-gradient(180deg,#7b98b4,#b8904c 55%,#5a4a3a)"></div><div><h3>The Lorem Lipsum</h3><p>It is a long established fact that a reader will be distracted by the read-</p></div></div>
    <div class="news-item"><div class="thumb" role="img" aria-label="Photo of a brick campus building" style="background:linear-gradient(180deg,#c9d6e0,#8a4a3e 45%,#6f8a4a)"></div><div><h3>The Lorem Lipsum</h3><p>It is a long established fact that a reader will be distracted by the read-</p></div></div>
    <div class="news-item"><div class="thumb" role="img" aria-label="Photo of a large stone building" style="background:linear-gradient(180deg,#a9b4bc,#6e6455 50%,#4a5a3a)"></div><div><h3>The Lorem Lipsum</h3><p>It is a long established fact that a reader will be distracted by the read-</p></div></div>
  </section>
  <h2 class="issues-title">CLICK BELOW TO FIND OUT WHAT YOU SHOULD KNOW ABOUT ISSUES THAT IMPACT OUR DAILY LIVES</h2>
  <div class="card" style="left:12px" role="img" aria-label="Photo of brick row houses"><div style="position:absolute;inset:0;background:linear-gradient(90deg,#7a3a34,#b4a48e 60%,#8a9a70)"></div><div class="card-band">Real estate Abatement</div></div>
  <div class="card" style="left:329px" role="img" aria-label="Photo of a man working at a desk"><div style="position:absolute;inset:0;background:linear-gradient(90deg,#3a2a20,#c8a060 50%,#6a5a3a)"></div><div class="card-band">Alimony Reform Act</div></div>
  <div class="card" style="left:641px" role="img" aria-label="Photo of a columned courthouse facade"><div style="position:absolute;inset:0;background:linear-gradient(180deg,#e6e6e6,#a8a8a4 50%,#7a7a76)"></div><div class="card-band">Immigration Reform</div></div>
</main>
<footer class="footer">Copyrights © 2013 Quenlow.example - All Rights Reserved. &nbsp;|&nbsp; Sitemap &nbsp;|&nbsp; Disclaimer</footer>
</body>
</html>
```